Single-sided business card for restaurant bellwether with new logo made on this site

Business card options with new logo including restaurant name, address, phone number and website. This business card is single-sided only and will be presented at the hostess desk for clients to take. I would like to see options based on a cream card background, a white card background, a yellow card background and a burgundy colored background. It needs to be elegant and traditional.

Target Market(s)

local and international crowd

Industry/Entity Type

restaurant

Contact Information for Business Card

address, website and phone number

Font styles to use
Serif

Colors
EE7325
F08F49
F5BC92
FAE3D3
FDF4ED

Requirements
Must have
• new logo, address, phone number, website
Should not have
• more than three colors

```html
<!DOCTYPE html>
<html lang="es">
<head>
<meta charset="utf-8">
<title>Bellwether — Business Card Options</title>
<link rel="stylesheet" href="https://fonts.googleapis.com/css2?family=Tinos:wght@400;700&display=swap">
<style>
  :root {
    --stage: #bcbcbc;
    --burgundy: #3f1c1e;
    --burgundy-decor: #553335;
    --yellow: #f7b32b;
    --yellow-decor: #e4a42d;
    --cream: #f6f1e1;
    --cream-decor: #e1dccb;
    --white: #ffffff;
    --white-decor: #e8e8e8;
    --ink: #3a1a1c;
    --paper-text: #ffffff;
    --accent: #f6b62d;
  }
  * { box-sizing: border-box; margin: 0; padding: 0; }
  html, body {
    width: 1200px;
    height: 795px;
    overflow: hidden;
    background: var(--stage);
  }
  .card-sheet {
    position: relative;
    width: 1200px;
    height: 795px;
  }
  .card {
    position: absolute;
    width: 515px;
    height: 295px;
    border-radius: 22px;
    overflow: hidden;
    box-shadow: 0 4px 8px rgba(0,0,0,0.25);
    font-family: "Tinos", "Times New Roman", serif;
    color: var(--ink);
    --icon: var(--ink);
    --icon-glyph: var(--white);
  }
  .card--burgundy { left: 65px;  top: 72px;  background: var(--burgundy); color: var(--paper-text); --decor: var(--burgundy-decor); --icon: var(--accent); --icon-glyph: var(--burgundy); --mark: var(--white); }
  .card--white    { left: 616px; top: 72px;  background: var(--white);  --decor: var(--white-decor);  --mark: var(--burgundy); }
  .card--yellow   { left: 65px;  top: 405px; background: var(--yellow); --decor: var(--yellow-decor); --icon-glyph: var(--yellow); --mark: var(--burgundy); }
  .card--cream    { left: 616px; top: 405px; background: var(--cream);  --decor: var(--cream-decor);  --icon-glyph: var(--cream); --mark: var(--burgundy); }

  .card__decor {
    position: absolute;
    left: 215px;
    top: 10px;
    width: 360px;
    height: 340px;
    border-radius: 50% 50% 0 0;
    background: radial-gradient(ellipse at 65% 70%, var(--decor) 0%, var(--decor) 45%, transparent 72%);
  }
  .brand {
    position: absolute;
    left: 18px;
    top: 22px;
    width: 115px;
    text-align: center;
  }
  .brand__square {
    display: block;
    width: 68px;
    height: 68px;
    margin: 0 auto 8px;
    background: var(--mark);
  }
  .brand__name {
    display: block;
    font-size: 21px;
    line-height: 23px;
    letter-spacing: 4px;
    text-transform: uppercase;
    font-weight: 400;
  }
  .address {
    position: absolute;
    left: 19px;
    top: 174px;
    font-size: 13.5px;
    line-height: 16.5px;
    letter-spacing: 0.3px;
  }
  .contacts {
    position: absolute;
    left: 19px;
    top: 216px;
    list-style: none;
    font-size: 13.5px;
    letter-spacing: 0.3px;
  }
  .contacts li {
    display: flex;
    align-items: center;
    height: 19px;
  }
  .contacts svg {
    width: 10px;
    height: 10px;
    margin-right: 5px;
    flex: none;
  }
  .icon-bg { fill: var(--icon); }
  .icon-glyph { fill: var(--icon-glyph); stroke: none; }
  .icon-line { fill: none; stroke: var(--icon-glyph); stroke-width: 1.2; }
</style>
</head>
<body>
<svg width="0" height="0" style="position:absolute">
  <defs>
    <symbol id="icon-phone" viewBox="0 0 10 10">
      <circle class="icon-bg" cx="5" cy="5" r="5"/>
      <path class="icon-glyph" d="M3 2.2 L4.2 3.4 L3.6 4.2 Q4.4 5.8 5.8 6.4 L6.6 5.8 L7.8 7 L7 7.9 Q3.2 7.4 2.1 3 Z"/>
    </symbol>
    <symbol id="icon-mail" viewBox="0 0 10 10">
      <circle class="icon-bg" cx="5" cy="5" r="5"/>
      <rect class="icon-glyph" x="2.3" y="3.2" width="5.4" height="3.6"/>
      <path class="icon-line" d="M2.4 3.3 L5 5.3 L7.6 3.3" style="stroke:var(--icon)"/>
    </symbol>
    <symbol id="icon-web" viewBox="0 0 10 10">
      <circle class="icon-bg" cx="5" cy="5" r="5"/>
      <circle class="icon-line" cx="5" cy="5" r="2.6"/>
      <path class="icon-line" d="M2.4 5 H7.6 M5 2.4 V7.6"/>
    </symbol>
  </defs>
</svg>

<main class="card-sheet">
  <!-- Burgundy option -->
  <article class="card card--burgundy">
    <div class="card__decor" role="img" aria-label="Large faint agave leaf illustration"></div>
    <div class="brand"><span class="brand__square"></span><span class="brand__name">Bell<br>wether</span></div>
    <p class="address">Jazmín 318 Colonia Arboleda,<br>Costa Verde Cp 70452</p>
    <ul class="contacts">
      <li><svg><use href="#icon-phone"/></svg>958-555-0142</li>
      <li><svg><use href="#icon-mail"/></svg>info@bellwether.com.mx</li>
      <li><svg><use href="#icon-web"/></svg>www.bellwether.com.mx</li>
    </ul>
  </article>

  <!-- White option -->
  <article class="card card--white">
    <div class="card__decor" role="img" aria-label="Large faint agave leaf illustration"></div>
    <div class="brand"><span class="brand__square"></span><span class="brand__name">Bell<br>wether</span></div>
    <p class="address">Jazmín 318 Colonia Arboleda,<br>Costa Verde Cp 70452</p>
    <ul class="contacts">
      <li><svg><use href="#icon-phone"/></svg>958-555-0142</li>
      <li><svg><use href="#icon-mail"/></svg>info@bellwether.com.mx</li>
      <li><svg><use href="#icon-web"/></svg>www.bellwether.com.mx</li>
    </ul>
  </article>

  <!-- Yellow option -->
  <article class="card card--yellow">
    <div class="card__decor" role="img" aria-label="Large faint agave leaf illustration"></div>
    <div class="brand"><span class="brand__square"></span><span class="brand__name">Bell<br>wether</span></div>
    <p class="address">Jazmín 318 Colonia Arboleda,<br>Costa Verde Cp 70452</p>
    <ul class="contacts">
      <li><svg><use href="#icon-phone"/></svg>958-555-0142</li>
      <li><svg><use href="#icon-mail"/></svg>info@bellwether.com.mx</li>
      <li><svg><use href="#icon-web"/></svg>www.bellwether.com.mx</li>
    </ul>
  </article>

  <!-- Cream option -->
  <article class="card card--cream">
    <div class="card__decor" role="img" aria-label="Large faint agave leaf illustration"></div>
    <div class="brand"><span class="brand__square"></span><span class="brand__name">Bell<br>wether</span></div>
    <p class="address">Jazmín 318 Colonia Arboleda,<br>Costa Verde Cp 70452</p>
    <ul class="contacts">
      <li><svg><use href="#icon-phone"/></svg>958-555-0142</li>
      <li><svg><use href="#icon-mail"/></svg>info@bellwether.com.mx</li>
      <li><svg><use href="#icon-web"/></svg>www.bellwether.com.mx</li>
    </ul>
  </article>
</main>
</body>
</html>
```